Business Association needs street banner design promoting business district.

We are a business association that manages a commercial district of small family owned businesses. We would like to install banners (30 inches wide by 60 inches long) on street lights. The banners will include our logo and the name of the sponsor (we will need a space for the sponsor information). We will also need a space to include a photo of the sponsoring business (this space needs to be large). The banners are intended to promote the local small businesses. For more information on our organization, our web site is www.larkmoorba.org.

Target Market(s)

Member businesses and customers.

Industry/Entity Type

Small Business

Font styles to use
Sans Serif

Requirements
Must have
• Any images or type must be large enough for pedestrians to read from a distance. Brights colors. No copy 4 inches from top or bottom (the banners will be folded and sewn). These banners will be installed on street lights (see example image in files). Please design banner in Adobe Illustrator.
• Text on banner: "Welcome to City Heights!" Please include logo on banner.

```html
<!DOCTYPE html>
<html lang="en">
<head>
<meta charset="utf-8">
<title>Welcome To City Heights – Street Banner</title>
<link rel="stylesheet" href="https://fonts.googleapis.com/css2?family=Cinzel:wght@700;900&family=Questrial&display=swap">
<style>
  :root {
    --paper: #ffffff;
    --ink: #111111;
    --banner-green: #0dfa78;
    --fold-light: #6ee89c;
    --fold-dark: #1f8a4c;
    --photo-green: #1c7a4b;
    --frame: #ffffff;
    --badge: #f6c21c;
  }
  html, body {
    margin: 0;
    padding: 0;
    overflow: hidden;
    background: var(--paper);
  }
  .banner {
    position: relative;
    width: 1200px;
    height: 2324px;
    overflow: hidden;
    background: var(--paper);
  }
  .banner__art {
    position: absolute;
    inset: 0;
    width: 1200px;
    height: 2324px;
  }
  .headline {
    position: absolute;
    left: 169px;
    top: 270px;
    width: 860px;
    margin: 0;
    text-align: center;
    font-family: "Cinzel", serif;
    font-weight: 900;
    color: var(--ink);
    line-height: 1;
  }
  .headline__welcome {
    display: block;
    font-size: 74px;
    letter-spacing: 2px;
    padding-bottom: 12px;
    border-bottom: 4px solid var(--ink);
  }
  .headline__place {
    display: block;
    font-size: 112px;
    letter-spacing: 1px;
    padding-top: 14px;
  }
  .association {
    position: absolute;
    left: 90px;
    top: 1838px;
    width: 400px;
    text-align: center;
  }
  .association__mark {
    display: block;
    width: 140px;
    height: 140px;
    margin: 0 auto 14px;
    border-radius: 50%;
    background: var(--badge);
  }
  .association__name {
    margin: 0;
    font-family: "Cinzel", serif;
    font-weight: 700;
    color: var(--paper);
    line-height: 1.05;
    font-size: 46px;
  }
  .association__name span {
    display: block;
    font-size: 27px;
    letter-spacing: 1px;
  }
  .divider {
    position: absolute;
    left: 500px;
    top: 1950px;
    width: 4px;
    height: 88px;
    background: var(--paper);
  }
  .web-address {
    position: absolute;
    left: 527px;
    top: 1965px;
    margin: 0;
    font-family: "Questrial", sans-serif;
    font-size: 47px;
    color: var(--paper);
    letter-spacing: 0.5px;
  }
</style>
</head>
<body>
<main class="banner">
  <svg class="banner__art" viewBox="0 0 1200 2324" xmlns="http://www.w3.org/2000/svg" aria-hidden="false">
    <defs>
      <linearGradient id="fold" x1="0" y1="0" x2="0.15" y2="1">
        <stop offset="0" stop-color="var(--fold-light)"/>
        <stop offset="0.55" stop-color="var(--fold-dark)"/>
        <stop offset="1" stop-color="var(--banner-green)"/>
      </linearGradient>
      <radialGradient id="curl" cx="0.55" cy="0.35" r="0.7">
        <stop offset="0" stop-color="#ffffff"/>
        <stop offset="1" stop-color="#e6e6e6"/>
      </radialGradient>
    </defs>
    <!-- green page -->
    <path class="page" d="M0 490 C 60 570 140 600 230 560 L 1200 948 L 1200 2324 L 0 2324 Z" fill="var(--banner-green)"/>
    <!-- peeled fold band -->
    <path class="page-fold" d="M40 500 C 120 520 190 500 260 505 C 560 640 900 800 1200 905 L 1200 955 C 900 840 560 700 230 590 C 140 600 70 560 40 500 Z" fill="url(#fold)"/>
    <!-- curled corner -->
    <path class="page-curl" d="M0 470 C 40 600 200 620 250 520 C 180 560 60 560 0 470 Z" fill="url(#curl)"/>
    <!-- sponsor photo area -->
    <polygon class="sponsor-photo" role="img" aria-label="Photo of the sponsoring business"
      points="116,715 1096,1012 1096,1793 116,1793"
      fill="var(--photo-green)" stroke="var(--frame)" stroke-width="4"/>
  </svg>

  <h1 class="headline">
    <span class="headline__welcome">Welcome To</span>
    <span class="headline__place">City Heights</span>
  </h1>

  <div class="association">
    <span class="association__mark"></span>
    <p class="association__name">LARKMOOR<span>BUSINESS ASSOCIATION</span></p>
  </div>

  <div class="divider"></div>
  <p class="web-address">www.larkmoorba.org</p>
</main>
</body>
</html>
```